ARC VOLLEY Business Card Project

I'd like to request a business card design for the new company I've launched.
The name of the company is "ARC VOLLEY" an indoor unmanned tennis practice facility.
We would like to see designs that use our brand identity color in the logo I've attached.
We hope to get the design with modern, luxurious and elegant tone and manner.
We hope the logo should not be too big.

Business card must have elements as below:
- Logo (One of the logos I've attached)
- Name (In Korean Text) : 박 서 윤
- Title (In Korean Text) : 대표
- Phone Number : 010-8472-3916
- Email Address : seoyun.park@arcvolley-example.co.kr
- Website : www.arcvolley-example.co.kr
- Instagram : arcvolley
- Address (In Korean text) : 경기도 용인시 수지구 풍덕천로 456 미래타워 5층 501호, 502호

Target Market(s)

Tennis amateurs in 20 to 40s

Industry/Entity Type

Sports, Hobby

Contact Information for Business Card

- Logo (One of the logos I've attached) - Name (In Korean Text) : 박 서 윤 - Title (In Korean Text) : 대표 - Phone Number : 010-8472-3916 - Email Address : seoyun.park@arcvolley-example.co.kr - Website : www.arcvolley-example.co.kr - Instagram : arcvolley - Address (In Korean text) : 경기도 용인시 수지구 풍덕천로 456 미래타워 5층 501호, 502호

Font styles to use
Sans Serif

Requirements
Must have
• Double sided
Nice to have
• Logo with intaglio or relief embossing
Should not have
• Logo should not be too big.

```html
<!DOCTYPE html>
<html lang="ko">
<head>
<meta charset="utf-8">
<title>ARC VOLLEY Business Card</title>
<link rel="stylesheet" href="https://fonts.googleapis.com/css2?family=Marcellus&family=Montserrat:wght@400&family=Nanum+Gothic&family=Nanum+Myeongjo&display=swap">
<style>
  :root {
    --brand-green: #2e5039;
    --paper: #ffffff;
    --backdrop: #b3b3b3;
  }
  html, body {
    margin: 0;
    width: 1000px;
    height: 1200px;
    overflow: hidden;
    background: var(--backdrop);
  }
  .card {
    position: absolute;
    left: 51px;
    width: 898px;
    height: 540px;
    background: var(--paper);
    overflow: hidden;
  }
  .card--front { top: 44px; }
  .card--back { top: 618px; }
  .card-waves {
    position: absolute;
    inset: 0;
    width: 100%;
    height: 100%;
  }
  .wave { fill: var(--brand-green); }
  .brand-name {
    position: absolute;
    left: 0;
    right: 0;
    text-align: center;
    font-family: "Marcellus", serif;
    font-size: 62px;
    line-height: 1;
    letter-spacing: 1px;
    margin: 0;
    font-weight: 400;
  }
  .card--front .brand-name { top: 104px; color: var(--brand-green); }
  .card--back .brand-name { top: 222px; color: var(--paper); }
  .person-name {
    position: absolute;
    top: 208px;
    left: 0;
    right: 0;
    text-align: center;
    margin: 0;
    font-family: "Nanum Myeongjo", serif;
    font-weight: 400;
    font-size: 50px;
    line-height: 1;
    color: var(--brand-green);
  }
  .person-title {
    position: absolute;
    top: 272px;
    left: 0;
    right: 0;
    text-align: center;
    margin: 0;
    font-family: "Nanum Gothic", sans-serif;
    font-size: 29px;
    line-height: 1;
    letter-spacing: 20px;
    padding-left: 20px;
    color: var(--brand-green);
  }
  .contact-list {
    position: absolute;
    left: 248px;
    top: 326px;
    margin: 0;
    padding: 0;
    list-style: none;
    font-family: "Montserrat", sans-serif;
    font-size: 18px;
    color: var(--brand-green);
  }
  .contact-item {
    display: flex;
    align-items: center;
    height: 27px;
    white-space: nowrap;
  }
  .contact-item--address {
    font-family: "Nanum Gothic", sans-serif;
    font-size: 17px;
  }
  .contact-icon {
    width: 16px;
    height: 16px;
    margin-right: 11px;
    flex: none;
    fill: none;
    stroke: var(--brand-green);
    stroke-width: 1.5;
  }
</style>
</head>
<body>
  <section class="card card--front">
    <svg class="card-waves" viewBox="0 0 1062 638" preserveAspectRatio="none" aria-hidden="true">
      <path class="wave" d="M0 0 H1062 V78 C900 40 720 25 560 48 C400 72 200 128 0 78 Z"/>
      <path class="wave" d="M0 582 C150 620 300 628 460 614 C650 596 820 570 1062 588 V638 H0 Z"/>
    </svg>
    <h1 class="brand-name">ARC VOLLEY</h1>
    <p class="person-name">박 서 윤</p>
    <p class="person-title">대표</p>
    <ul class="contact-list">
      <li class="contact-item">
        <svg class="contact-icon" viewBox="0 0 18 18" aria-hidden="true">
          <path d="M4 2 L7 5 L5.5 7 C6.5 9.5 8.5 11.5 11 12.5 L13 11 L16 14 L14 16 C8 16 2 10 2 4 Z"/>
        </svg>
        <span>010-8472-3916</span>
      </li>
      <li class="contact-item">
        <svg class="contact-icon" viewBox="0 0 18 18" aria-hidden="true">
          <rect x="1.5" y="4" width="15" height="10"/>
          <path d="M1.5 4 L9 10 L16.5 4 M1.5 14 L7 9 M16.5 14 L11 9"/>
        </svg>
        <span>seoyun.park@arcvolley-example.co.kr</span>
      </li>
      <li class="contact-item">
        <svg class="contact-icon" viewBox="0 0 18 18" aria-hidden="true">
          <circle cx="9" cy="9" r="7.5"/>
          <path d="M1.5 9 H16.5 M9 1.5 C5.5 5 5.5 13 9 16.5 M9 1.5 C12.5 5 12.5 13 9 16.5"/>
        </svg>
        <span>www.arcvolley-example.co.kr</span>
      </li>
      <li class="contact-item">
        <svg class="contact-icon" viewBox="0 0 18 18" aria-hidden="true">
          <rect x="2" y="2" width="14" height="14"/>
        </svg>
        <span>arcvolley</span>
      </li>
      <li class="contact-item contact-item--address">
        <svg class="contact-icon" viewBox="0 0 18 18" aria-hidden="true">
          <path d="M9 16.5 C5 11.5 3.5 9 3.5 6.5 A5.5 5.5 0 0 1 14.5 6.5 C14.5 9 13 11.5 9 16.5 Z"/>
          <circle cx="9" cy="6.5" r="2"/>
        </svg>
        <span>경기도 용인시 수지구 풍덕천로 456 미래타워 5층 501호, 502호</span>
      </li>
    </ul>
  </section>

  <section class="card card--back">
    <svg class="card-waves" viewBox="0 0 1062 638" preserveAspectRatio="none" aria-hidden="true">
      <path class="wave" d="M0 75 C200 20 400 10 600 50 C800 90 950 110 1062 75 V560 C900 610 700 592 500 562 C300 532 150 530 0 560 Z"/>
    </svg>
    <h2 class="brand-name">ARC VOLLEY</h2>
  </section>
</body>
</html>
```